International Hand & Body company needing a Hand cream tube design for the Retail market

I am wanting a modern design for a new range of 6 hand creams I will be launching in August. They need to compliment our range of wrapped soaps which you can see on www.plovane.com.au so am wanting clean designs. I am wanting a solid colour with a hand drawn organic feel line drawing in black elegantly placed wrapping around the label. I am wanting to focus on the colour and positioning of words and fonts. I like modern clean contemporary fonts. The final design needs to appeal to the broader female market.This may lead to range expansion if designs are well received.
Updates

These designs are not hitting the brief. They are too generic and look like a supermarket brand. Our brand is more boutique and this design needs to be modern and simple. I would like more solid colours and more modern designs. Without patterns.

Target Market(s)

Female aged 20 - 70

Requirements
Must have
• a modern contemporary design that will appeal to the masses.
• Please read attached brief.
Should not have
• a black botanical illustration, in a loose and organic design to match the fragrance.

```html
<!DOCTYPE html>
<html lang="en">
<head>
<meta charset="utf-8">
<title>plovane — Yuzu &amp; Sage Hand Cream</title>
<link rel="stylesheet" href="https://fonts.googleapis.com/css2?family=Open+Sans:wght@500&family=Oswald:wght@300;400;500&family=Arimo:wght@400;700&display=swap">
<style>
  :root {
    --backdrop: #d3d3d3;
    --sage: #5f9584;
    --sage-light: #86b1a3;
    --sage-dark: #3e7363;
    --sage-text: #6a988a;
    --label: #eeeff0;
    --label-shade: #d9dadd;
    --ink: #2f3132;
    --ink-soft: #4a4c4e;
  }
  * { margin: 0; padding: 0; box-sizing: border-box; }
  html, body { width: 1170px; height: 1200px; overflow: hidden; background: var(--backdrop); }
  .canvas { position: relative; width: 1170px; height: 1200px; }
  .tube { position: absolute; top: 240px; width: 280px; height: 710px; }
  .tube--front { left: 297px; }
  .tube--back { left: 612px; }
  .tube__shape { position: absolute; inset: 0; }
  .tube__text { position: absolute; left: 0; width: 280px; text-align: center; }

  .brand { font-family: "Open Sans", sans-serif; font-weight: 500; font-size: 34px; letter-spacing: 5px; color: var(--ink); }
  .front-brand { top: 106px; }
  .back-brand { top: 78px; }

  .claims { top: 141px; font-family: "Oswald", sans-serif; font-weight: 400; font-size: 12.5px; line-height: 17.5px; color: #f2f6f4; letter-spacing: .2px; }

  .scent { top: 340px; font-family: "Oswald", sans-serif; font-weight: 400; font-size: 26px; color: var(--sage-text); letter-spacing: .5px; }
  .tagline { top: 417px; font-family: "Oswald", sans-serif; font-weight: 300; font-size: 13.5px; line-height: 16.5px; color: var(--ink-soft); }
  .tagline b { font-weight: 400; }
  .product-type { top: 488px; left: 85px; width: 110px; border-top: 1px solid var(--sage-text); border-bottom: 1px solid var(--sage-text); padding: 3px 0 2px; font-family: "Oswald", sans-serif; font-weight: 300; font-size: 22px; color: var(--sage-text); line-height: 28px; }
  .origin { top: 535px; font-family: "Arimo", sans-serif; font-weight: 700; font-size: 7px; color: var(--sage-text); letter-spacing: .2px; }
  .volume { top: 546px; font-family: "Arimo", sans-serif; font-size: 10.5px; color: var(--sage-text); }

  .ingredients { top: 233px; left: 46px; width: 188px; font-family: "Oswald", sans-serif; font-weight: 300; font-size: 10.2px; line-height: 15.9px; color: var(--sage-text); }
  .ingredients b { font-weight: 500; }
  .warnings { top: 427px; left: 40px; width: 200px; font-family: "Oswald", sans-serif; font-weight: 500; font-size: 10px; line-height: 16px; color: var(--ink-soft); }
  .warnings .use { display: block; margin-top: 3px; }
  .skin-types { top: 502px; left: 52px; width: 176px; border-top: 1px solid var(--ink-soft); padding-top: 2px; font-family: "Arimo", sans-serif; font-weight: 700; font-size: 7.5px; color: var(--ink-soft); }
  .icon-row { position: absolute; top: 518px; left: 51px; width: 166px; display: flex; justify-content: space-between; align-items: center; }
  .icon-square { width: 19px; height: 19px; border: 2px solid var(--ink-soft); border-radius: 4px; }
  .icon-square--filled { background: var(--ink-soft); }
  .icon-circle { width: 18px; height: 18px; border-radius: 50%; background: var(--ink-soft); }
  .icon-ring { width: 18px; height: 18px; border-radius: 50%; border: 2px solid var(--ink-soft); }
  .batch-code { position: absolute; top: 551px; left: 223px; transform: rotate(-90deg); transform-origin: left top; font-family: "Arimo", sans-serif; font-size: 5px; line-height: 6px; white-space: nowrap; color: var(--ink-soft); }
  .address { top: 543px; left: 52px; width: 176px; border-top: 1px solid var(--ink-soft); border-bottom: 1px solid var(--ink-soft); padding: 2px 0 1px; font-family: "Arimo", sans-serif; font-weight: 700; font-size: 6px; color: var(--ink-soft); }
  .contact { top: 560px; left: 52px; width: 176px; border-bottom: 1px solid var(--ink-soft); padding: 2px 0 2px; font-family: "Arimo", sans-serif; font-weight: 700; font-size: 7px; color: var(--ink-soft); }
</style>
</head>
<body>
<main class="canvas">

  <svg width="0" height="0" style="position:absolute" aria-hidden="true">
    <defs>
      <linearGradient id="sageBand" x1="0" x2="1" y1="0" y2="0">
        <stop offset="0" stop-color="#7aa898"/>
        <stop offset=".5" stop-color="#5f9584"/>
        <stop offset="1" stop-color="#3f7464"/>
      </linearGradient>
      <linearGradient id="labelBand" x1="0" x2="1" y1="0" y2="0">
        <stop offset="0" stop-color="#d8d9dc"/>
        <stop offset=".35" stop-color="#f2f3f4"/>
        <stop offset="1" stop-color="#dcdde0"/>
      </linearGradient>
      <linearGradient id="capBand" x1="0" x2="1" y1="0" y2="0">
        <stop offset="0" stop-color="#6c9e8e"/>
        <stop offset=".45" stop-color="#5a8f7f"/>
        <stop offset="1" stop-color="#3b6d5e"/>
      </linearGradient>
      <g id="tubeBody">
        <path d="M0 0 H280 L230 604 H50 Z" fill="url(#labelBand)"/>
        <path d="M0 0 H280 L261.5 224 H18.5 Z" fill="url(#sageBand)"/>
        <rect x="0" y="0" width="280" height="30" fill="#6b9c8c"/>
        <path d="M18.3 226 H261.7" stroke="#ffffff" stroke-width="3"/>
        <path d="M50 604 H230 V700 Q230 707 223 707 H57 Q50 707 50 700 Z" fill="url(#capBand)"/>
        <path d="M50 604 H230 V610 H50 Z" fill="#44786a" opacity=".7"/>
        <path d="M112 707 V680 Q112 672 120 672 H160 Q168 672 168 680 V707" fill="none" stroke="#3a6a5c" stroke-width="2" opacity=".6"/>
      </g>
    </defs>
  </svg>

  <section class="tube tube--front" aria-label="Hand cream tube, front">
    <svg class="tube__shape" viewBox="0 0 280 710" width="280" height="710" aria-hidden="true"><use href="#tubeBody"/></svg>
    <div class="tube__text brand front-brand">plovane</div>
    <h1 class="tube__text scent">YUZU &amp; SAGE</h1>
    <p class="tube__text tagline">a nourishing <b>non-greasy</b><br>hand cream <b>to keep skin</b><br><b>soft &amp; hydrated.</b></p>
    <h2 class="tube__text product-type">HAND CREAM</h2>
    <p class="tube__text origin">MADE IN AUSTRALIA</p>
    <p class="tube__text volume">35mL ℮ 1.18 fl. oz.</p>
  </section>

  <section class="tube tube--back" aria-label="Hand cream tube, back">
    <svg class="tube__shape" viewBox="0 0 280 710" width="280" height="710" aria-hidden="true"><use href="#tubeBody"/></svg>
    <div class="tube__text brand back-brand">plovane</div>
    <p class="tube__text claims">NO SULFATES<br>NO PARABENS<br>NO MINERAL OILS<br>NO ARTIFICAL COLOURS</p>
    <p class="tube__text ingredients"><b>INGREDIENTS:</b> AQUA, HELIANTHUS ANNUUS SEED (SUNFLOWER) OIL, STEARIC ACID, GLYCERIN, CETEARYL ALCOHOL, BEESWAX, GLYCERYL STEARATE, DIMETHICONE, PRUNUS AMYGDALUS DULCIS (ALMOND) OIL, PARFUM, ACRYLATES, PHENOXYETHANOL, TRIETHANOLAMINE, TOCOPHERYL ACETATE, CAPRYLYL GLYCOL, SODIUM PCA, DISODIUM EDTA, ALOE BARBADENSIS LEAF JUICE (ALOE VERA) POWDER, HEXYLENE GLYCOL, THEOBROMA CACAO SEED (COCOA) BUTTER, COCOS NUCIFERA (COCONUT) OIL, BUTYROSPERMUM PARKII (SHEA) BUTTER</p>
    <p class="tube__text warnings">DISCONTINUE USE IF IRRITATION OCCURS,<br>KEEP AWAY FROM CHILDREN.<br>AVOID CONTACT WITH EYES.<span class="use">MASSAGE INTO CLEAN DRY SKIN AS NEEDED.</span></p>
    <p class="tube__text skin-types">SUITABLE FOR ALL SKIN TYPES</p>
    <div class="icon-row" aria-hidden="true">
      <span class="icon-square"></span>
      <span class="icon-square icon-square--filled"></span>
      <span class="icon-circle"></span>
      <span class="icon-ring"></span>
      <span class="icon-square"></span>
      <span class="icon-circle"></span>
    </div>
    <span class="batch-code">Code: 418736</span>
    <p class="tube__text address">Unit 5 / 12 Marlow Street Brighton VIC 3186</p>
    <p class="tube__text contact">plovane.com.au &nbsp;&nbsp;|&nbsp;&nbsp; sales@plovane.com.au</p>
  </section>

</main>
</body>
</html>
```